Business Card & Stationary for Belmora Yards
1 sided business card and stationary
Modern
Trevor Hollis
WPMB Certified Applicator
48260 Pinecrest
Overland Park, KS 66213
trevor@belmorayards.com
belmorayards.com
I like business cards that use the symbols for phone, web, and email rather than using the words.
I would also like to list my services on the card. They could all be listed on one line at the bottom of the card with bullets between them or wherever they may fit best with the rest of the design.
"Fertilization"
"Weed Control"
"Aeration"
"Verticutting"
"Seeding"
Should be plain white with nothing printed on it. (1 sided business card please)
Logo to use on card

```html
<!DOCTYPE html>
<html lang="en">
<head>
<meta charset="utf-8">
<title>Belmora Yards Stationery</title>
<link rel="stylesheet" href="https://fonts.googleapis.com/css2?family=Open+Sans:wght@400;600;700&display=swap">
<style>
:root{
  --stage:#2b2b2d;
  --paper:#ffffff;
  --paper-shade:#eef0ec;
  --green:#5c9b2b;
  --green-dark:#3f7a1c;
  --brown:#6a3a1f;
  --ink:#4a4a4a;
  --muted:#9a9a9a;
  --faint:#eef2ea;
}
*{margin:0;padding:0;box-sizing:border-box}
html,body{width:1200px;height:559px;overflow:hidden}
body{background:var(--stage);font-family:"Open Sans",Arial,sans-serif;color:var(--ink);position:relative}

.logo-mark{display:flex;align-items:center;gap:.3em;color:var(--green-dark);font-weight:700;white-space:nowrap;line-height:1}
.logo-mark i{width:.6em;height:.6em;border-radius:50%;background:var(--green);display:block;flex:none}

.brand{position:absolute;left:40px;top:128px;width:220px;text-align:center}
.brand .logo-mark{justify-content:center;color:var(--paper);font-size:28px}
.brand-tagline{margin-top:10px;font-size:9px;color:var(--muted);letter-spacing:.5px}

.card{position:absolute;left:36px;top:264px;width:232px;height:120px;background:var(--paper);overflow:hidden}
.card .logo-mark{position:absolute;left:12px;top:30px;font-size:12px}
.card-person{position:absolute;left:122px;top:18px;font-size:6px;line-height:1.4;white-space:nowrap}
.card-person strong{color:var(--green-dark);font-size:9px;display:block}
.card-contact{position:absolute;left:122px;top:46px;font-size:5.5px;line-height:1.55;white-space:nowrap}
.card-services{position:absolute;left:0;right:0;bottom:0;height:14px;background:var(--green);color:var(--paper);font-size:5.5px;font-weight:600;display:flex;align-items:center;justify-content:center;white-space:nowrap}

.letterhead{position:absolute;left:293px;top:34px;width:350px;height:470px;background:var(--paper)}
.letterhead-edge{position:absolute;left:0;top:0;bottom:0;width:4px;background:var(--green)}
.letterhead .logo-mark{position:absolute;left:18px;top:26px;font-size:18px}
.letterhead-address{position:absolute;left:226px;top:20px;font-size:5.5px;line-height:1.6;color:var(--muted);border-left:1px solid var(--paper-shade);padding-left:5px;white-space:nowrap}
.letterhead-watermark{position:absolute;left:112px;top:190px;width:130px;height:130px;border-radius:50%;background:var(--faint)}
.letterhead-footer{position:absolute;left:0;right:0;bottom:12px;text-align:center;font-size:5.5px;color:var(--muted)}

.envelope{position:absolute;width:440px;height:220px;background:var(--paper);overflow:hidden}
.envelope svg{position:absolute;left:0;top:0}
.env-back{left:705px;top:110px}
.env-mid{left:712px;top:160px}
.env-front{left:696px;top:284px}
.env-dot{position:absolute;width:18px;height:18px;border-radius:50%;background:var(--paper);left:211px}
.env-back .env-dot{background:var(--green);top:40px}
.env-mid .env-dot{top:62px}
.env-front .env-dot{top:26px}
.env-front .logo-mark{position:absolute;left:22px;top:100px;font-size:16px}
.env-address{position:absolute;left:22px;top:124px;font-size:5.5px;color:var(--muted)}
.env-watermark{position:absolute;right:36px;bottom:24px;width:80px;height:80px;border-radius:50%;background:var(--faint)}
.env-web{position:absolute;left:0;right:0;bottom:10px;text-align:center;font-size:5.5px;color:var(--muted)}
</style>
</head>
<body>

<section class="brand">
  <div class="logo-mark"><i></i>Belmora Yards</div>
  <div class="brand-tagline">Residential Programs</div>
</section>

<article class="card">
  <div class="logo-mark"><i></i>Belmora Yards</div>
  <div class="card-person"><strong>Trevor Hollis</strong>WPMB Certified Applicator</div>
  <div class="card-contact">
    48260 Pinecrest<br>Overland Park, KS 66213<br>
    &#9742; (913) 555-0148<br>
    &#9993; trevor@belmorayards.com<br>
    &#9675; belmorayards.com
  </div>
  <div class="card-services">Fertilization &bull; Weed Control &bull; Aeration &bull; Verticutting &bull; Seeding</div>
</article>

<article class="letterhead">
  <div class="letterhead-edge"></div>
  <div class="logo-mark"><i></i>Belmora Yards</div>
  <div class="letterhead-address">48260 Pinecrest<br>Overland Park, KS 66213<br>(913) 555-0148<br>trevor@belmorayards.com</div>
  <div class="letterhead-watermark"></div>
  <div class="letterhead-footer">belmorayards.com</div>
</article>

<div class="envelope env-back">
  <svg width="440" height="220" viewBox="0 0 440 220"><path d="M0 0 L220 110 L440 0 Z" fill="var(--paper-shade)"/></svg>
  <span class="env-dot"></span>
</div>
<div class="envelope env-mid">
  <svg width="440" height="220" viewBox="0 0 440 220"><path d="M0 0 H440 V30 L220 120 L0 30 Z" fill="var(--brown)"/></svg>
  <span class="env-dot"></span>
</div>
<div class="envelope env-front">
  <svg width="440" height="220" viewBox="0 0 440 220"><path d="M0 0 H440 V20 Q220 110 0 20 Z" fill="var(--green)"/></svg>
  <span class="env-dot"></span>
  <div class="logo-mark"><i></i>Belmora Yards</div>
  <div class="env-address">48260 Pinecrest, Overland Park, KS 66213</div>
  <div class="env-watermark"></div>
  <div class="env-web">belmorayards.com</div>
</div>

</body>
</html>
```